Book Cover Design Project

A non-fiction book on child protection, specifically... keeping young children safe from predators and keeping teenagers safe from themselves.

Title:
Under Our Roof

Subtitle:
A Guide To Keeping Your Children Safe

Author:
Martin Kellerby

```html
<!DOCTYPE html>
<html lang="en">
<head>
<meta charset="UTF-8">
<title>Under Our Roof — Book Cover</title>
<link rel="stylesheet" href="https://fonts.googleapis.com/css2?family=Anton&display=swap">
<style>
  :root {
    --page-bg: #ffffff;
    --sky-top: #f8ebc4;
    --sky-mid: #f3d593;
    --haze: #efc980;
    --sand: #d99a4a;
    --shore: #9e5e26;
    --ink: #0d0d0d;
    --cream: #fbeccb;
  }
  * { margin: 0; padding: 0; box-sizing: border-box; }
  html, body {
    width: 1036px;
    height: 1200px;
    overflow: hidden;
    background: var(--page-bg);
  }
  .cover {
    position: absolute;
    left: 158px;
    top: 100px;
    width: 720px;
    height: 1000px;
    overflow: hidden;
    background: linear-gradient(to bottom, var(--sky-top) 0%, var(--sky-mid) 45%, var(--haze) 60%);
  }
  .cover-photo {
    position: absolute;
    left: 0;
    right: 0;
    top: 560px;
    bottom: 0;
    background: linear-gradient(
      to bottom,
      rgba(239, 201, 128, 0) 0%,
      var(--haze) 18%,
      var(--sand) 62%,
      var(--shore) 100%
    );
  }
  .cover-title {
    position: absolute;
    top: 170px;
    left: 0;
    width: 100%;
    text-align: center;
    font-family: "Anton", "Impact", sans-serif;
    font-weight: 400;
    font-size: 108px;
    line-height: 1;
    letter-spacing: -1px;
    color: var(--ink);
  }
  .cover-subtitle {
    position: absolute;
    top: 400px;
    left: 0;
    width: 100%;
    text-align: center;
    font-family: "Anton", "Impact", sans-serif;
    font-size: 40px;
    line-height: 1.5;
    color: var(--ink);
  }
  .cover-author {
    position: absolute;
    bottom: 46px;
    left: 0;
    width: 100%;
    text-align: center;
    font-family: "Anton", "Impact", sans-serif;
    font-size: 36px;
    letter-spacing: 1px;
    color: var(--cream);
  }
</style>
</head>
<body>
  <main class="cover">
    <div class="cover-photo" role="img" aria-label="Photo: hazy golden beach at sunset with an adult and a small child walking along the shore in silhouette"></div>
    <h1 class="cover-title">Under Our Roof</h1>
    <p class="cover-subtitle">A Guide To Keeping<br>Your Children Safe</p>
    <p class="cover-author">Martin Kellerby</p>
  </main>
</body>
</html>
```